I need a business card design for a Boutique Pilates studio.

I would like to see designs similar to the one that I have uploaded.
thinking between two slogans:
'No ordinary place'
'Not so ordinary'

Contact Information for Business Card

KiVa Pilates

```html
<!DOCTYPE html>
<html lang="en">
<head>
<meta charset="utf-8">
<title>KiVa Pilates – Business Card</title>
<link rel="stylesheet" href="https://fonts.googleapis.com/css2?family=Great+Vibes&family=Open+Sans:wght@300;400&display=swap">
<style>
  :root {
    --backdrop-light: #e2e3e6;
    --backdrop-dark: #b3b4b8;
    --card: #444444;
    --accent: #f2d200;
    --shadow: rgba(0, 0, 0, 0.35);
  }
  * { box-sizing: border-box; margin: 0; padding: 0; }
  html, body {
    width: 1200px;
    height: 939px;
    overflow: hidden;
  }
  body {
    background: radial-gradient(ellipse at 50% 50%, var(--backdrop-light) 0%, var(--backdrop-dark) 85%);
    display: flex;
    flex-direction: column;
    align-items: center;
    justify-content: center;
    gap: 56px;
  }
  .card {
    width: 640px;
    height: 366px;
    background: var(--card);
    color: var(--accent);
    box-shadow: 0 6px 14px var(--shadow);
    position: relative;
  }
  /* Front */
  .card-front {
    display: flex;
    align-items: center;
    justify-content: center;
  }
  .brand-name {
    font-family: "Open Sans", sans-serif;
    font-weight: 400;
    font-size: 56px;
    letter-spacing: 2px;
    line-height: 1;
  }
  /* Back */
  .card-back {
    display: flex;
    align-items: center;
    justify-content: center;
    gap: 22px;
  }
  .person {
    display: flex;
    flex-direction: column;
    align-items: flex-end;
  }
  .person-name {
    font-family: "Great Vibes", cursive;
    font-size: 50px;
    line-height: 1;
  }
  .person-role {
    font-family: "Open Sans", sans-serif;
    font-size: 15px;
    letter-spacing: 1px;
    margin-top: 6px;
  }
  .divider {
    width: 1.5px;
    height: 86px;
    background: var(--accent);
  }
  .contact-list {
    list-style: none;
    font-family: "Open Sans", sans-serif;
    font-size: 15px;
    letter-spacing: 0.5px;
    line-height: 1.6;
  }
  .contact-list li {
    display: flex;
    align-items: center;
    gap: 7px;
  }
  .contact-icon {
    width: 12px;
    height: 12px;
    fill: var(--accent);
    stroke: var(--accent);
    flex: none;
  }
</style>
</head>
<body>

  <section class="card card-front" aria-label="Card front">
    <h1 class="brand-name">KiVa Pilates</h1>
  </section>

  <section class="card card-back" aria-label="Card back">
    <div class="person">
      <p class="person-name">Mara Ellison</p>
      <p class="person-role">Owner</p>
    </div>
    <div class="divider"></div>
    <ul class="contact-list">
      <li>
        <svg class="contact-icon" viewBox="0 0 12 12" aria-hidden="true">
          <path stroke="none" d="M2.4 0.6 L4.2 2.8 L3.2 4.2 C3.9 5.8 5.9 7.9 7.8 8.8 L9.2 7.8 L11.4 9.6 L10.2 11.4 C5.4 11.2 0.8 6.6 0.6 1.8 Z"/>
        </svg>
        0400 318 562
      </li>
      <li>
        <svg class="contact-icon" viewBox="0 0 12 12" aria-hidden="true">
          <rect x="0.5" y="2" width="11" height="8" stroke="none"/>
          <path d="M0.8 2.4 L6 6.6 L11.2 2.4" fill="none" stroke="#444444" stroke-width="1.2"/>
        </svg>
        info@KiVaPilates.com.au
      </li>
      <li>
        <svg class="contact-icon" viewBox="0 0 12 12" aria-hidden="true">
          <g fill="none" stroke-width="1">
            <circle cx="6" cy="6" r="5.2"/>
            <ellipse cx="6" cy="6" rx="2.3" ry="5.2"/>
            <path d="M0.8 6 H11.2 M1.6 3.4 H10.4 M1.6 8.6 H10.4"/>
          </g>
        </svg>
        KiVaPilates.com.au
      </li>
    </ul>
  </section>

</body>
</html>
```